Postcard Design Spring Trails D to D

Residential Real Estate, we want to implement a mail campaign in an specific geographic area.We want to include Market information on the area and statistics of the real estate market.This piece is going to be deliver via mail service door to door.

Target Market(s)

Home owners that might be interested in selling their houses

Industry/Entity Type

Real Estate

Font styles to use
Sans Serif

Colors
ec1f27
f78f20

Requirements
Must have
• Attractive look
• Include the information that we just sent to you
• Clear graphics and tables
• Must include clear information about our group

```html
<!DOCTYPE html>
<html lang="en">
<head>
<meta charset="utf-8">
<title>Spring Trails – October Results 2015</title>
<link href="https://fonts.googleapis.com/css2?family=Open+Sans:ital,wght@0,400;0,600;0,700;1,400;1,600&family=Patrick+Hand&display=swap" rel="stylesheet">
<style>
  :root{
    --brand-red:#c8223f;
    --title-gray:#6d6e71;
    --ink:#222;
    --paper:#fff;
    --swoosh-gray:#a7a9ac;
    --swoosh-light:#d9dadc;
    --bg:#ffffff;
  }
  *{margin:0;padding:0;box-sizing:border-box}
  html,body{width:1200px;height:900px;overflow:hidden;background:var(--bg)}
  .postcard{position:relative;width:1200px;height:900px;background:var(--paper);overflow:hidden;font-family:"Open Sans",sans-serif;color:var(--ink)}
  .backdrop{position:absolute;inset:0;width:1200px;height:900px}
  .headline{position:absolute;right:613px;top:2px;text-align:right;white-space:nowrap}
  .headline__title{font-size:80px;font-weight:700;line-height:1.05;letter-spacing:-1px}
  .headline__title .accent{color:var(--brand-red);font-style:italic}
  .headline__title .neutral{color:var(--title-gray)}
  .headline__sub{font-size:35px;font-weight:700;color:var(--title-gray);line-height:1;margin-top:-2px;letter-spacing:.5px}
  .headline__tag{position:absolute;left:20px;top:140px;font-size:19px;color:#222;white-space:nowrap}
  .hero-photo{position:absolute;left:627px;top:0;width:573px;height:157px;background:linear-gradient(180deg,#c9d3dd 0%,#8e98a4 45%,#6f9c3a 70%,#5e9a22 100%)}
  .letter{position:absolute;left:40px;top:330px;width:535px;height:600px;background:var(--paper);transform:rotate(-4deg);transform-origin:top left;box-shadow:0 4px 14px rgba(0,0,0,.28);padding:60px 40px 0 72px;font-family:"Patrick Hand",sans-serif;font-size:21px;line-height:1.08;color:var(--ink)}
  .letter__greeting{font-size:22px;font-weight:700;margin-bottom:14px}
  .letter p{margin-bottom:22px}
  .letter__curl{position:absolute;left:-1px;bottom:-1px;width:150px;height:140px}
  .facts{position:absolute;left:680px;top:205px;width:500px}
  .facts__heading{text-align:center;color:var(--brand-red);font-size:23px;font-weight:600;font-style:italic;margin-bottom:12px}
  .facts__table{margin-left:40px;border-collapse:collapse;font-size:24px;font-style:italic}
  .facts__table td{padding:0;line-height:1.3}
  .facts__table td.value{text-align:right;padding-left:30px}
  .quote{position:absolute;left:680px;top:440px;width:500px;text-align:center;color:var(--brand-red);font-size:29px;font-style:italic;line-height:1.3}
  .brokerage{position:absolute;left:650px;top:755px;display:flex;flex-direction:column;gap:2px}
  .brokerage__name{display:flex;align-items:center;gap:8px;font-size:22px;font-weight:600;color:var(--brand-red)}
  .brokerage__mark{width:18px;height:18px;background:var(--brand-red)}
  .brokerage__office{font-size:13px;color:#333;padding-left:26px}
  .team{position:absolute;left:880px;top:740px;text-align:right}
  .team__name{font-size:34px;color:var(--brand-red);font-weight:400;border-bottom:2px solid var(--brand-red);line-height:1.15}
  .team__sub{font-size:14px;color:var(--brand-red);font-style:italic}
  .website{position:absolute;left:132px;top:836px;color:#fff;font-size:26px;font-style:italic}
</style>
</head>
<body>
<div class="postcard">
  <svg class="backdrop" viewBox="0 0 1200 900" aria-hidden="true">
    <path d="M0 770 C300 740 700 760 1200 690" fill="none" stroke="var(--swoosh-light)" stroke-width="2"/>
    <path d="M0 780 C300 752 700 772 1200 702" fill="none" stroke="var(--swoosh-light)" stroke-width="2"/>
    <path d="M0 790 C300 764 700 784 1200 714" fill="none" stroke="var(--swoosh-light)" stroke-width="2"/>
    <path d="M0 800 C300 776 700 796 1200 728 L1200 770 C800 820 350 790 0 812 Z" fill="var(--swoosh-light)"/>
    <path d="M0 812 C350 790 800 830 1200 770 L1200 820 C800 880 400 810 0 830 Z" fill="var(--swoosh-gray)"/>
    <path d="M0 832 C400 812 800 890 1200 835 L1200 900 L0 900 Z" fill="var(--brand-red)"/>
    <path d="M700 860 C900 880 1050 860 1200 835" fill="none" stroke="#fff" stroke-width="6"/>
  </svg>

  <header class="headline">
    <h1 class="headline__title"><span class="accent">Spring</span> <span class="neutral">Trails</span></h1>
    <p class="headline__sub">October Results 2015</p>
  </header>
  <p class="headline__tag">Market Report of single family sold and active homes</p>

  <div class="hero-photo" role="img" aria-label="Photo of a large grey two-storey family home with a green front lawn"></div>

  <article class="letter">
    <p class="letter__greeting">Dear Spring Trails Neighbor:</p>
    <p>We expect that this information will be useful for you to learn about the Real estate market in your neighborhood.</p>
    <p>There are 28 properties “Active for Sale” on the market, with an average price of $303,589 USD and $101.06 USD per sf. Average time on market for sale 63 days.</p>
    <p>In process, “Pending to Close” are 9 houses at average price of $252,808 USD with a sale price of $103.11 per sf. with 34 Days on market.</p>
    <p>The past 6 Months market behavior was as follows: 97 Houses sold at average price of $263,545 with a sale price / sqf. of $100.50</p>
    <svg class="letter__curl" viewBox="0 0 150 140" aria-hidden="true">
      <defs>
        <linearGradient id="curlShade" x1="0" y1="1" x2="1" y2="0">
          <stop offset="0" stop-color="#9a9a9a"/>
          <stop offset=".5" stop-color="#f4f4f4"/>
          <stop offset="1" stop-color="#cfcfcf"/>
        </linearGradient>
      </defs>
      <path d="M0 0 L0 140 L150 140 Z" fill="var(--bg)"/>
      <path d="M0 0 C20 70 60 120 150 140 C90 100 40 90 0 0 Z" fill="url(#curlShade)"/>
    </svg>
  </article>

  <section class="facts">
    <h2 class="facts__heading">Spring Trails 2014 Facts</h2>
    <table class="facts__table">
      <tr><td>Single Family Properties</td><td class="value">1,667</td></tr>
      <tr><td>Median Square Feet</td><td class="value">2,568</td></tr>
      <tr><td>Median Lot Square Feet</td><td class="value">7,689</td></tr>
      <tr><td>Median Year Built</td><td class="value">2007</td></tr>
    </table>
  </section>

  <blockquote class="quote">“We will be glad to meet with you and have the opportunity to help you with your Real Estate requirements”</blockquote>

  <div class="brokerage">
    <span class="brokerage__name"><span class="brokerage__mark"></span>Hartwell Realty</span>
    <span class="brokerage__office">north hills &amp; cedar</span>
  </div>

  <div class="team">
    <div class="team__name">The Marlowe Group</div>
    <div class="team__sub">Real Estate</div>
  </div>

  <p class="website">www.themarlowegroup.com</p>
</div>
</body>
</html>
```